Zielgruppe
Ich biete die neue Dienstleistung an, Schulungen zu überprüfen auf deren Inhalt und mittels einem Zertifikat zu bestätigen, dass die geprüfte Schulung allen notwendigen Anforderungen der Normen und Regelwerke in Sachen Gaswarntechnik entspricht.
Daraufhin darf der Geprüfte (Schulungsanbieter/Schulungsgesellschaften) mit meinem Siegel für seine Schulumng werben.
Dies wird ausschießlich für Schulungen von Gaswarntechnik angeboten von mir angeboten. Das Siegel existiert schon und das Zertifikat sollte hier mit integriert werden.
Aufgabenstellung
Ich stelle mir ein hochwertiges Design vor, eine einzige DIN A4 Seite und 3D-Effekt. Es muss richtig teuer, hochwertig und modern aussehen, sodass man auch fühlt, dass es eine Wertigkeit hat. Das bestehende Siegel sollte integriert werden.
Ich brauche Textteile die ich anpassen kann. Zum einen muss ein Bereich da sein wo ich die Bezeichnung der geprüften Schulungen unterbringen kann, dann ein Bereich wo ich etwas zum Inhalt/Prüfung schreiben kann und natürlich Datum und Unterschriftsfeld. Das Zertifikat hat immer eine Gültigkeit von 2 Jahren ab Ausstellungsdatum.
Es sollten meine Farben eingsetzt werden. Zum einen ist dies
Ultramarinblau RAL 5002 RGB= rot 0/grün 56/ blau 123
Weiß
gelb (nicht genau definiert), rapsgelb RAL 1021/1023
Schriftart Verdana
Das Design sollte an mein bestehndes Design in Sachen Logo/Homepage angelehnt sein.

```html
<!DOCTYPE html>
<html lang="de">
<head>
<meta charset="utf-8">
<title>Zertifikat – Musterschulung</title>
<link href="https://fonts.googleapis.com/css2?family=Open+Sans:wght@400;600;800&family=Nunito+Sans:wght@300;400&display=swap" rel="stylesheet">
<style>
  :root {
    --gold-dark: #c07a0c;
    --gold: #e9a416;
    --gold-light: #f8c43a;
    --cream: #fbf5e6;
    --blue: #0f4a7f;
    --blue-deep: #00387b;
    --white: #ffffff;
  }
  * { margin: 0; padding: 0; box-sizing: border-box; }
  html, body { width: 848px; height: 1200px; overflow: hidden; background: var(--white); }
  .certificate {
    position: relative; width: 848px; height: 1200px;
    background: var(--cream);
    font-family: "Nunito Sans", Verdana, sans-serif;
    color: var(--blue);
  }
  .frame-outer {
    position: absolute; left: 39px; top: 39px; width: 770px; height: 1121px;
    border: 6px solid var(--gold);
    border-color: var(--gold-dark) var(--gold) var(--gold-dark) var(--gold);
  }
  .frame-inner {
    position: absolute; left: 53px; top: 53px; width: 742px; height: 1093px;
    border: 1.5px solid var(--gold);
  }
  .sheet {
    position: absolute; left: 74px; top: 74px; width: 700px; height: 1051px;
    background: var(--white);
  }
  .title {
    position: absolute; left: 0; top: 110px; width: 848px; text-align: center;
    font-family: "Open Sans", Verdana, sans-serif; font-weight: 800;
    font-size: 108px; line-height: 1; letter-spacing: -1px;
    background: linear-gradient(90deg, var(--gold-dark), var(--gold-light) 25%, var(--gold-dark) 45%, var(--gold-light) 65%, var(--gold-dark));
    -webkit-background-clip: text; background-clip: text; color: transparent;
  }
  .rule {
    position: absolute; left: 110px; width: 628px; height: 2px;
    background: linear-gradient(90deg, transparent, var(--gold) 20%, var(--gold) 80%, transparent);
  }
  .course-name {
    position: absolute; left: 0; top: 284px; width: 848px; text-align: center;
    font-family: "Open Sans", Verdana, sans-serif; font-weight: 600;
    font-size: 47px; line-height: 1; color: var(--blue);
  }
  .intro {
    position: absolute; left: 124px; top: 384px; width: 601px;
    font-family: "Open Sans", Verdana, sans-serif; font-size: 14.6px; line-height: 20.5px;
    letter-spacing: -0.1px;
    text-align: justify; text-align-last: justify; color: var(--blue-deep);
  }
  .seal {
    position: absolute; left: 359px; top: 457px; width: 131px; height: 195px;
    background: linear-gradient(160deg, var(--gold-light), var(--gold-dark));
  }
  .details {
    position: absolute; left: 124px; top: 686px; width: 600px;
    font-size: 11.2px; line-height: 15.4px; font-weight: 300;
    text-align: justify; color: var(--blue-deep);
  }
  .place-date {
    position: absolute; left: 0; top: 816px; width: 842px; text-align: center;
    font-size: 11px; color: var(--blue-deep);
  }
  .signature {
    position: absolute; left: 293px; top: 842px; width: 262px; height: 38px;
    background: linear-gradient(90deg, rgba(15,74,127,0.15), rgba(15,74,127,0.3), rgba(15,74,127,0.15));
    border-radius: 4px;
  }
  .brand {
    position: absolute; left: 0; top: 972px; width: 848px;
    display: flex; align-items: center; justify-content: center; gap: 14px;
  }
  .brand-dot { width: 62px; height: 62px; border-radius: 50%; background: var(--blue); }
  .brand-name {
    font-family: "Open Sans", Verdana, sans-serif; font-weight: 600;
    font-size: 40px; color: var(--blue);
  }
  .validity {
    position: absolute; left: 0; top: 1090px; width: 848px; text-align: center;
    font-size: 8.5px; color: var(--blue-deep);
  }
</style>
</head>
<body>
<main class="certificate">
  <div class="frame-outer"></div>
  <div class="frame-inner"></div>
  <div class="sheet"></div>

  <h1 class="title">ZERTIFIKAT</h1>
  <div class="rule" style="top:266px"></div>
  <h2 class="course-name">MUSTERSCHULUNG</h2>
  <div class="rule" style="top:356px"></div>

  <p class="intro">Lorem ipsum dolor sit amet, consectetuer adipiscing elit. Aenean commodo ligula eget dolor. Aenean massa. Cum sociis natoque penatibus et magnis dis parturie asol.</p>

  <div class="seal" role="img" aria-label="Prüfsiegel für Schulungen in Gaswarntechnik"></div>

  <p class="details">Lorem ipsum dolor sit amet, consectetuer adipiscing elit. Aenean commodo ligula eget dolor. Aenean massa. Cum sociis natoque penatibus et magnis dis parturient montes, nascetur ridiculus mus. Donec quam felis, ultricies nec, pellentesque eu, pretium quis, sem. Nulla consequat massa quis enim. Donec pede justo, fringilla vel, aliquet nec, vulputate eget, arcu. In enim justo, rhoncus ut, imperdiet a, venenatis vitae, justo. Nullam dictum felis eu pede. Lorem ipsum dolor sit amet, consectetuer adipiscing elit. Aenean commodo ligula eget dolor. Aenean massa. Cum sociis natoque penatibus et magnis dis parturient montes, nascetur ridiculus mus. Donec quam felis, ultricies nec, pellentesque eu, pretium quis, sem. Nulla consequat massa quis enim. Donec pede justo, fringilla vel, aliquet nec, vulputate.</p>

  <p class="place-date">Musterstadt, den 22.03.2023</p>
  <div class="signature" role="img" aria-label="Unterschrift"></div>

  <div class="rule" style="top:942px"></div>
  <div class="brand">
    <span class="brand-dot"></span>
    <span class="brand-name">Gasmelder-Kontor</span>
  </div>
  <div class="rule" style="top:1065px"></div>

  <p class="validity">Dieses Zertifikat hat eine Gültigkeit von 2 Jahren ab Ausstellungsdatum.</p>
</main>
</body>
</html>
```